Mr. Kelpie Restaurant Menu Design

I would like for you to please create a menu design for my seafood restaurant called Mr. Kelpie. I uploaded the logo of my restaurant and would like the same colors and font to be used on the menu. The headings of my menu should include the following:
What's your catch?
What's your sauce?
How "Hot" can you go?
Medium?
Mild?
Wild?
Soups
Paella
Katsu
Add Ons
Sweet Cravings
Thirsty?
It would be nice to see something creative and simple preferably one page.
I already uploaded my logo on the brief section.
Thank you.
Target Market(s)
Family friendly
Industry/Entity Type
Seafood Restaurant
Look and feel

```html
<!DOCTYPE html>
<html lang="en">
<head>
<meta charset="utf-8">
<title>Mr. Kelpie Restaurant Menu</title>
<link rel="stylesheet" href="https://fonts.googleapis.com/css2?family=Fredoka:wght@500;600;700&family=Oswald:wght@500&family=Open+Sans:wght@400;600&display=swap">
<style>
  :root {
    --orange: #f47b20;
    --navy: #1c2b4b;
    --ink: #2b2b2b;
    --grey: #5c5c5c;
    --white: #ffffff;
    --photo-warm: #d9893f;
    --photo-cool: #c9b48a;
  }
  * { margin: 0; padding: 0; box-sizing: border-box; }
  html, body { width: 849px; height: 1200px; overflow: hidden; background: var(--white); }
  .menu { position: relative; width: 849px; height: 1200px; overflow: hidden; font-family: "Open Sans", sans-serif; color: var(--ink); }

  .header-art { position: absolute; left: 0; top: 0; width: 849px; height: 300px; }
  .brand { position: absolute; left: 0; width: 849px; text-align: center; top: 140px;
    font-family: "Fredoka", sans-serif; font-weight: 600; font-size: 34px; color: var(--navy); line-height: 1.2; }

  .questions { position: absolute; left: 0; width: 849px; top: 212px; text-align: center;
    font-family: "Oswald", sans-serif; font-weight: 500; font-size: 23px; color: var(--navy); letter-spacing: 0.5px; word-spacing: 4px; }
  .heat { position: absolute; left: 0; width: 849px; top: 252px; text-align: center;
    font-family: "Fredoka", sans-serif; font-weight: 700; font-size: 56px; color: var(--orange); line-height: 1;
    text-shadow: 2px 2px 0 var(--navy), -1px -1px 0 var(--navy), 1px -1px 0 var(--navy), -1px 1px 0 var(--navy); word-spacing: 10px; }

  .section-title { position: absolute; height: 42px; padding: 0 22px; border-radius: 0 21px 21px 0;
    background: var(--orange); color: var(--white); font-family: "Fredoka", sans-serif; font-weight: 600;
    font-size: 30px; line-height: 42px; }
  .section-title.right { border-radius: 21px 0 0 21px; }

  .dish { position: absolute; width: 380px; height: 60px; }
  .dish-photo { position: absolute; left: 0; top: 0; width: 58px; height: 58px; border-radius: 50%;
    background: radial-gradient(circle at 40% 35%, var(--photo-cool), var(--photo-warm)); border: 3px solid var(--white);
    box-shadow: 0 0 0 2px var(--orange); }
  .dish-name { position: absolute; left: 80px; top: 0; font-family: "Fredoka", sans-serif; font-weight: 600;
    font-size: 21px; color: var(--orange); line-height: 26px; }
  .dish-price { position: absolute; right: 0; top: 0; font-family: "Fredoka", sans-serif; font-weight: 500;
    font-size: 21px; color: var(--ink); line-height: 26px; }
  .dish-desc { position: absolute; left: 80px; top: 27px; width: 220px; font-size: 12.5px; line-height: 15px; color: var(--grey); }

  .drinks-photo { position: absolute; left: 428px; top: 976px; width: 120px; height: 130px; border-radius: 14px;
    background: linear-gradient(160deg, #f3d27a, #e08a3c 60%, #c04a2a); }
  .drink { position: absolute; left: 570px; width: 230px; font-family: "Fredoka", sans-serif; font-weight: 500; font-size: 20px; color: var(--ink); }
  .drink span { position: absolute; right: 0; }

  .footer { position: absolute; left: 0; top: 1120px; width: 849px; height: 80px; background: var(--orange); color: var(--white); }
  .contact { position: absolute; left: 34px; font-family: "Fredoka", sans-serif; font-weight: 500; font-size: 19px; display: flex; align-items: center; gap: 10px; }
  .find-us { position: absolute; left: 470px; top: 26px; font-family: "Fredoka", sans-serif; font-weight: 600; font-size: 22px; }
  .social { position: absolute; top: 24px; width: 32px; height: 32px; border-radius: 6px; background: var(--white); opacity: 0.9; }
</style>
</head>
<body>
<main class="menu">
  <svg class="header-art" viewBox="0 0 849 300" aria-hidden="true">
    <rect x="0" y="0" width="849" height="210" fill="#f47b20"/>
    <path d="M0 150 Q 424 30 849 150 L 849 210 L 0 210 Z" fill="#ffffff"/>
    <path d="M0 120 Q 424 0 849 120" fill="none" stroke="#ffffff" stroke-width="6" opacity="0.6"/>
    <path d="M0 95 Q 424 -25 849 95" fill="none" stroke="#ffffff" stroke-width="3" opacity="0.4"/>
  </svg>
  <h1 class="brand">Mr. Kelpie Restaurant</h1>

  <p class="questions">WHAT'S YOUR CATCH? &nbsp; WHAT'S YOUR SAUCE? &nbsp; HOW "HOT" CAN YOU GO?</p>
  <p class="heat">Medium? Mild? Wild?</p>

  <h2 class="section-title" style="left:0; top:410px;">Soups</h2>
  <div class="dish" style="left:34px; top:462px;">
    <div class="dish-photo" role="img" aria-label="Photo of crab tortilla soup"></div>
    <h3 class="dish-name">Crab Tortilla Soup</h3><span class="dish-price">$6.25</span>
    <p class="dish-desc">Poached Crab, honey tomato, avocado, tuna tapenade</p>
  </div>
  <div class="dish" style="left:34px; top:536px;">
    <div class="dish-photo" role="img" aria-label="Photo of tomato soup"></div>
    <h3 class="dish-name">Tomato Soup</h3><span class="dish-price">$7.55</span>
    <p class="dish-desc">A velvety smooth tomato and cream soup</p>
  </div>
  <div class="dish" style="left:34px; top:610px;">
    <div class="dish-photo" role="img" aria-label="Photo of lobster soup"></div>
    <h3 class="dish-name">Lobster Soup</h3><span class="dish-price">$8.25</span>
    <p class="dish-desc">A velvety smooth lobster and cream soup</p>
  </div>

  <h2 class="section-title" style="left:0; top:686px;">Paella</h2>
  <div class="dish" style="left:34px; top:738px;">
    <div class="dish-photo" role="img" aria-label="Photo of seafood paella"></div>
    <h3 class="dish-name">Paella</h3><span class="dish-price">$35.25</span>
    <p class="dish-desc">Spanish dish made with combinations of rice , vegetables, meat, chicken, and seafood</p>
  </div>
  <div class="dish" style="left:34px; top:818px;">
    <div class="dish-photo" role="img" aria-label="Photo of paella pan"></div>
    <h3 class="dish-name">Paella</h3><span class="dish-price">$30.25</span>
    <p class="dish-desc">Spanish dish made with combinations of rice , vegetables, meat, chicken, and seafood</p>
  </div>

  <h2 class="section-title" style="left:0; top:908px;">Katsu</h2>
  <div class="dish" style="left:34px; top:960px;">
    <div class="dish-photo" role="img" aria-label="Photo of prawns katsu"></div>
    <h3 class="dish-name">Prawns Katsu</h3><span class="dish-price">$10.25</span>
    <p class="dish-desc">Prawn, potato croquette, edamame, rice</p>
  </div>
  <div class="dish" style="left:34px; top:1036px;">
    <div class="dish-photo" role="img" aria-label="Photo of fish katsu"></div>
    <h3 class="dish-name">Fish Katsu</h3><span class="dish-price">$12.25</span>
    <p class="dish-desc">Fish, potato croquette, edamame.</p>
  </div>

  <h2 class="section-title right" style="right:0; top:410px; width:380px;">Add Ons</h2>
  <div class="dish" style="left:430px; top:462px;">
    <div class="dish-photo" role="img" aria-label="Photo of robian salad"></div>
    <h3 class="dish-name">Robian Salad</h3><span class="dish-price">$8.25</span>
    <p class="dish-desc">Arugula, halloumi and pomegranate</p>
  </div>
  <div class="dish" style="left:430px; top:528px;">
    <div class="dish-photo" role="img" aria-label="Photo of salmon roulade"></div>
    <h3 class="dish-name">Salmon roulade</h3><span class="dish-price">$9.25</span>
    <p class="dish-desc">Basil chocolate, marinated daikon, citra leaves</p>
  </div>
  <div class="dish" style="left:430px; top:594px;">
    <div class="dish-photo" role="img" aria-label="Photo of pan fried scallops"></div>
    <h3 class="dish-name">Pan fried Scallops</h3><span class="dish-price">$7.25</span>
    <p class="dish-desc">Stuffed calamari, squid ink risotto, micro herbs</p>
  </div>

  <h2 class="section-title right" style="right:0; top:668px; width:380px;">Sweet Cravings</h2>
  <div class="dish" style="left:430px; top:720px;">
    <div class="dish-photo" role="img" aria-label="Photo of homemade tiramisu"></div>
    <h3 class="dish-name">Homemade Tiramisu</h3><span class="dish-price">$8.25</span>
    <p class="dish-desc">Layers of mascarpone cheese and lady fingers soaked in coffee</p>
  </div>
  <div class="dish" style="left:430px; top:786px;">
    <div class="dish-photo" role="img" aria-label="Photo of Jamaica mud cake"></div>
    <h3 class="dish-name">Jamaica Mud Cake</h3><span class="dish-price">$7.25</span>
    <p class="dish-desc">Dark chocolate sponge with a middle layer of chocolate ganache</p>
  </div>
  <div class="dish" style="left:430px; top:852px;">
    <div class="dish-photo" role="img" aria-label="Photo of bianco e nero dessert"></div>
    <h3 class="dish-name">Bianco e Nero</h3><span class="dish-price">$8.25</span>
    <p class="dish-desc">Profiterole filled with vanilla custard and covered in milk chocolate</p>
  </div>

  <h2 class="section-title right" style="right:0; top:920px; width:380px;">Thirsty?</h2>
  <div class="drinks-photo" role="img" aria-label="Photo of assorted drinks"></div>
  <p class="drink" style="top:980px;">Filter Coffe<span>$5.25</span></p>
  <p class="drink" style="top:1012px;">Tea<span>$6.25</span></p>
  <p class="drink" style="top:1044px;">Beer<span>$4.25</span></p>
  <p class="drink" style="top:1076px;">Cocktail<span>$7.25</span></p>

  <footer class="footer">
    <p class="contact" style="top:10px;">
      <svg width="18" height="22" viewBox="0 0 18 22" aria-hidden="true"><path d="M9 1a7 7 0 0 0-7 7c0 5 7 13 7 13s7-8 7-13a7 7 0 0 0-7-7z" fill="#fff"/><circle cx="9" cy="8" r="2.6" fill="#f47b20"/></svg>
      Your Address
    </p>
    <p class="contact" style="top:42px;">
      <svg width="18" height="20" viewBox="0 0 18 20" aria-hidden="true"><path d="M4 1l3 4-2 3c1 3 3 5 6 6l3-2 3 3-2 3C8 19 0 11 1 3z" fill="#fff"/></svg>
      0145-7720-318
    </p>
    <p class="find-us">Find us @Mr.Kelpie</p>
    <span class="social" style="left:680px;"></span>
    <span class="social" style="left:720px;"></span>
    <span class="social" style="left:760px;"></span>
    <span class="social" style="left:800px;"></span>
  </footer>
</main>
</body>
</html>
```